Business Card for Managing Partner Investment Fund

To create a business card template for an investment fund manager. Business card should be more professional in nature, not too colorful, more upscale, and created using the attached logos and fund name files. I would prefer a black or gray color scheme, but am open to the use of color as well. I would prefer a double sided business card, but open to single sided business card designs as well. The business card should include: name, title, and contact information, as well as logo and company name. I would prefer a more stream-lined, simple business card design.
Updates
Address: 4136 NE 19th Ter. Ocala, FL 34470
Email: travis48@quillnet-mail.com
Phone: 561-374-9186
Title: managing partner
Name: Travis Whitlow
Fund Name: Emberfall Capital
Logos can be found in files attached to the brief
Target Market(s)
potential investors, other fund managers
Industry/Entity Type
Finance
Contact Information for Business Card
Name on card: Travis Whitlow
Title: Managing Partner
Font styles to use
Colors
Designer to choose colors to be used in the design.
Requirements
Must have
- Phone number
- email address
- physical address
- title
- name
- logo
- Fund name
Nice to have
- simple layout
Should not have
- too many colors, busy fonts,

```html
<!DOCTYPE html>
<html lang="en">
<head>
<meta charset="utf-8">
<title>Emberfall Capital — Business Card</title>
<link href="https://fonts.googleapis.com/css2?family=Cinzel:wght@500;600&family=Tinos&display=swap" rel="stylesheet">
<style>
  :root {
    --bg: #e4e4e4;
    --card-dark: #2a2627;
    --card-light: #ffffff;
    --ink: #1c1a1b;
    --ink-soft: #8a8a8a;
    --paper-text: #ffffff;
  }
  * { margin: 0; padding: 0; box-sizing: border-box; }
  html, body {
    width: 1200px; height: 900px; overflow: hidden;
    background: var(--bg);
  }
  .stage {
    width: 1200px; height: 900px;
    display: flex; flex-direction: column;
    align-items: center; justify-content: center;
    gap: 56px;
  }
  .card {
    width: 640px; height: 366px;
    border-radius: 22px;
    display: flex; flex-direction: column;
    align-items: center; justify-content: center;
    text-align: center;
    box-shadow: 0 6px 18px rgba(0,0,0,0.18);
  }
  .card--back { background: var(--card-dark); color: var(--paper-text); }
  .card--front { background: var(--card-light); color: var(--ink); }

  .company {
    font-family: "Cinzel", serif;
    font-weight: 600;
    line-height: 1.05;
    letter-spacing: 0.06em;
    text-transform: uppercase;
  }
  .card--back .company { font-size: 44px; }
  .card--front .company { font-size: 38px; margin-bottom: 14px; }
  .company span { display: block; }
  .company .company-sub { font-size: 0.72em; letter-spacing: 0.22em; }

  .person-name {
    font-family: "Cinzel", serif;
    font-weight: 600;
    font-size: 21px;
    letter-spacing: 0.08em;
    text-transform: uppercase;
  }
  .person-title {
    font-family: "Cinzel", serif;
    font-weight: 500;
    font-size: 15px;
    letter-spacing: 0.1em;
    text-transform: uppercase;
    color: var(--ink-soft);
    margin-bottom: 8px;
  }
  .contact {
    font-family: "Tinos", serif;
    font-size: 16px;
    line-height: 1.45;
  }
  .contact .sep { padding: 0 6px; }
</style>
</head>
<body>
  <main class="stage">
    <section class="card card--back" aria-label="Card back">
      <h1 class="company"><span>Emberfall</span><span class="company-sub">Capital</span></h1>
    </section>

    <section class="card card--front" aria-label="Card front">
      <h2 class="company"><span>Emberfall</span><span class="company-sub">Capital</span></h2>
      <p class="person-name">Travis Whitlow</p>
      <p class="person-title">Managing Partner</p>
      <address class="contact" style="font-style: normal;">
        <div>4136 NE 19th Ter. Ocala, FL 34470</div>
        <div>561-374-9186<span class="sep">|</span>travis48@quillnet-mail.com</div>
      </address>
    </section>
  </main>
</body>
</html>
```